R & T Summit Construction Business Card ideas

We want a business card to represents our company in a way that looks professional but is also a business card that is unique!

Industry/Entity Type

Construction Company

Contact Information for Business Card

open to all design ideas, just want to be able to see different options to choose from in either color or grayscale.

Requirements
Must have
• Our names and phone numbers
• Nolan Pritchett 512-804-2271
• Curtis Hale 512-693-1804
• Business logo

```html
<!DOCTYPE html>
<html lang="en">
<head>
<meta charset="utf-8">
<title>R &amp; T Summit Construction – Business Card</title>
<link rel="stylesheet" href="https://fonts.googleapis.com/css2?family=Crimson+Pro:wght@400;600&display=swap">
<style>
  :root {
    --backdrop: #e9e6e1;
    --card-dark: #0b0b0b;
    --card-dark-edge: #1c1c1c;
    --card-light: #f7f7f5;
    --ink-dark: #2a2a2a;
    --ink-muted: #6b6b6b;
    --ink-light: #ffffff;
  }
  * { box-sizing: border-box; margin: 0; padding: 0; }
  html, body {
    width: 1200px;
    height: 1022px;
    overflow: hidden;
    background: var(--backdrop);
    font-family: "Crimson Pro", Georgia, serif;
  }
  .sheet {
    width: 1200px;
    height: 1022px;
    display: flex;
    flex-direction: column;
    align-items: center;
    justify-content: center;
    gap: 44px;
  }
  .card {
    width: 760px;
    height: 434px;
    border-radius: 18px;
    position: relative;
    overflow: hidden;
    box-shadow: 0 10px 28px rgba(0,0,0,0.18);
  }
  /* Front */
  .card-front {
    background: linear-gradient(160deg, var(--card-dark-edge) 0%, var(--card-dark) 55%);
    display: flex;
    align-items: center;
    justify-content: center;
  }
  .brand {
    text-align: center;
    color: var(--ink-light);
  }
  .brand-name {
    font-weight: 600;
    font-size: 46px;
    letter-spacing: 2px;
    text-transform: uppercase;
    line-height: 1;
    color: var(--ink-light);
  }
  .brand-rule {
    display: block;
    width: 560px;
    height: 2px;
    margin: 16px auto 0;
    background: var(--ink-light);
  }
  /* Back */
  .card-back {
    background: var(--card-light);
  }
  .contacts {
    position: absolute;
    left: 64px;
    bottom: 70px;
    list-style: none;
  }
  .contact + .contact { margin-top: 6px; }
  .contact-name {
    font-weight: 600;
    font-size: 30px;
    letter-spacing: 2px;
    text-transform: uppercase;
    color: var(--ink-dark);
    line-height: 1.15;
  }
  .contact-phone {
    display: flex;
    align-items: center;
    gap: 8px;
    font-weight: 400;
    font-size: 26px;
    letter-spacing: 1px;
    color: var(--ink-muted);
    line-height: 1.15;
  }
  .phone-icon { width: 14px; height: 16px; fill: var(--ink-muted); }
</style>
</head>
<body>
  <main class="sheet">
    <section class="card card-front" aria-label="Card front">
      <div class="brand">
        <div class="brand-name">R &amp; T Summit Construction</div>
        <span class="brand-rule"></span>
      </div>
    </section>

    <section class="card card-back" aria-label="Card back">
      <ul class="contacts">
        <li class="contact">
          <div class="contact-name">Nolan Pritchett</div>
          <div class="contact-phone">
            <svg class="phone-icon" viewBox="0 0 14 16" aria-hidden="true"><path d="M4.2 0.6 2 1.6C0.4 2.5 0 4.6 1.1 7.5c1.3 3.4 3.6 6.3 6.2 7.9 1.4.8 2.8.7 3.7-.2l1.3-1.3-2.7-2.9-1.6 1.1C6.6 11 5 8.7 4.6 6.8l1.6-.9z"/></svg>
            <span>512-804-2271</span>
          </div>
        </li>
        <li class="contact">
          <div class="contact-name">Curtis Hale</div>
          <div class="contact-phone">
            <svg class="phone-icon" viewBox="0 0 14 16" aria-hidden="true"><path d="M4.2 0.6 2 1.6C0.4 2.5 0 4.6 1.1 7.5c1.3 3.4 3.6 6.3 6.2 7.9 1.4.8 2.8.7 3.7-.2l1.3-1.3-2.7-2.9-1.6 1.1C6.6 11 5 8.7 4.6 6.8l1.6-.9z"/></svg>
            <span>512-693-1804</span>
          </div>
        </li>
      </ul>
    </section>
  </main>
</body>
</html>
```